Book Cover

Hello!
I need someone to design a book cover with the title, subtitle and one of the photos attached.

- Title: Beyond the Grey Hours - By Corwin Ashdale
- Subtitle: A Steady Handbook for finding calm and strength after hard news.

```html
<!DOCTYPE html>
<html lang="en">
<head>
<meta charset="utf-8">
<title>Beyond the Grey Hours — Corwin Ashdale</title>
<link rel="stylesheet" href="https://fonts.googleapis.com/css2?family=Oswald:wght@700&family=Josefin+Sans:wght@600&family=Great+Vibes&family=Montserrat:wght@600&display=swap">
<style>
  :root {
    --band: #000000;
    --white: #ffffff;
    --navy: #1a2a4a;
    --red: #d0151c;
    --sky-top: #dfe8ef;
    --sky-mid: #c9cfc9;
    --field-warm: #b89060;
    --field-deep: #7a5a38;
    --jacket: #23407a;
  }
  * { margin: 0; padding: 0; box-sizing: border-box; }
  html, body { width: 750px; height: 1200px; overflow: hidden; background: #ffffff; }
  .cover { position: relative; width: 750px; height: 1200px; overflow: hidden; }

  .cover-photo {
    position: absolute; left: 0; top: 88px; width: 750px; height: 1029px;
    background:
      radial-gradient(ellipse 260px 420px at 200px 900px, var(--jacket) 0%, rgba(35,64,122,0.85) 55%, rgba(35,64,122,0) 100%),
      linear-gradient(180deg, var(--sky-top) 0%, #e8ece9 30%, var(--sky-mid) 48%, var(--field-warm) 70%, var(--field-deep) 100%);
  }

  .title-band {
    position: absolute; left: 0; top: 0; width: 750px; height: 88px;
    background: var(--band);
    display: flex; align-items: center; justify-content: center;
  }
  .title {
    font-family: "Oswald", sans-serif; font-weight: 700;
    color: var(--white); font-size: 50px; letter-spacing: 1px;
    text-transform: uppercase; line-height: 1;
  }

  .subtitle { position: absolute; left: 0; top: 0; width: 750px; height: 700px; }
  .subtitle-lead {
    position: absolute; left: 90px; top: 188px; width: 590px;
    font-family: "Josefin Sans", sans-serif; font-weight: 600;
    color: var(--navy); font-size: 33px; letter-spacing: 0.5px;
    text-transform: uppercase; text-align: center; white-space: nowrap;
  }
  .subtitle-script {
    position: absolute; left: 50px; top: 232px; width: 680px;
    font-family: "Great Vibes", cursive; color: var(--navy);
    font-size: 120px; line-height: 1; text-align: center; white-space: nowrap;
  }
  .subtitle-script .small { font-size: 52px; }
  .subtitle-accent {
    position: absolute; left: 300px; top: 355px; width: 440px;
    font-family: "Great Vibes", cursive; color: var(--red);
    font-size: 190px; line-height: 1; text-align: center; white-space: nowrap;
  }
  .subtitle-tag {
    position: absolute; left: 354px; top: 608px; width: 376px; height: 56px;
    background: var(--navy); border-radius: 10px;
    display: flex; align-items: center; justify-content: center;
    font-family: "Josefin Sans", sans-serif; font-weight: 600;
    color: var(--white); font-size: 30px; text-transform: uppercase; letter-spacing: 0.5px;
    padding-top: 4px;
  }

  .author-band {
    position: absolute; left: 0; top: 1117px; width: 750px; height: 83px;
    background: var(--band);
    display: flex; align-items: center; justify-content: flex-end; padding-right: 34px;
  }
  .author {
    font-family: "Montserrat", sans-serif; font-weight: 600;
    color: var(--white); font-size: 38px;
  }
</style>
</head>
<body>
  <main class="cover">
    <div class="cover-photo" role="img" aria-label="Photograph of a grey-haired man in a blue jacket standing in an autumn field of dry grasses and bare trees under a pale sky"></div>

    <header class="title-band">
      <h1 class="title">Beyond the Grey Hours</h1>
    </header>

    <section class="subtitle">
      <p class="subtitle-lead">A Steady Handbook for finding</p>
      <p class="subtitle-script">calm <span class="small">and</span> strength</p>
      <p class="subtitle-accent">after</p>
      <p class="subtitle-tag">hard news.</p>
    </section>

    <footer class="author-band">
      <p class="author">By Corwin Ashdale</p>
    </footer>
  </main>
</body>
</html>
```